Company Business Card Design Project - Revamp the image of an old construction company.

We need a business card designed for a new company in Australia.

Type of business is Commercial Roofing & Painting.

Medium will be brushed black metal card that can/will be acid etched to a brushed steel silver, acid die cut and two printed colours of our choice which will be white and pantone orange.

We have hopes that the design will be simple, modern and represent with a quick glance what our company does.

Please read instructions carefully in must have box any questions please ask.

If you are interested in this job please look at other job that we have which is very similar with logo and design

Please have a look at the things that can be done with metals cards on yondle images for inspiration.

Target Market(s)

Business owners, commercial property development Men from 25-70 years of age.

Industry/Entity Type

Construction

Requirements
Must have
• Front of card:

Must use the company logo and name provided as attachment (see below kestrel mark construction_black_background).

the words -Commercial Painting and Roofing- must be on front of card

details needed on front or back depending on your design

Name
position
email
mobile

all details can be on front with a cool design to be etched on the back of card or to keep front simple you can put all detail on back of card, I will leave the lay out to you.

Colours in logo are

Pantone 144 C Orange
Pantone 11-0601 White
Pantone 7539 C Gray
Pantone 426 C Black

However black will be the base of black metal card. Gray will be replaced with the etching in card revealing the silver. Orange and white will be printed on card.

Please have fun!!
Should not have
• Please don't clutter the card
No fonts smaller then 7 points

```html
<!DOCTYPE html>
<html lang="en">
<head>
<meta charset="utf-8">
<title>Kestrel Mark Construction – Business Card</title>
<link rel="stylesheet" href="https://fonts.googleapis.com/css2?family=Michroma&family=Saira+Semi+Condensed:wght@400;500&display=swap">
<style>
  :root {
    --bg: #d9d6d2;
    --card: #111112;
    --card-edge: #1c1c1e;
    --orange: #f39a1e;
    --white: #f4f4f2;
    --steel: #8d8f93;
  }
  * { margin: 0; padding: 0; box-sizing: border-box; }
  html, body { width: 1200px; height: 960px; overflow: hidden; }
  body {
    background: var(--bg);
    position: relative;
    font-family: "Saira Semi Condensed", "Arial Narrow", sans-serif;
  }
  .card {
    position: absolute;
    left: 250px;
    width: 700px;
    height: 400px;
    background: linear-gradient(135deg, var(--card-edge), var(--card) 60%);
    border-radius: 0 80px 0 80px;
    box-shadow: 0 14px 30px rgba(0,0,0,0.25);
    color: var(--white);
  }
  .card--front { top: 60px; }
  .card--back { top: 500px; }

  .brand {
    position: absolute;
    left: 60px;
    top: 70px;
    display: flex;
    align-items: center;
    gap: 18px;
  }
  .brand__mark {
    flex: none;
    width: 40px;
    height: 40px;
    background: var(--orange);
  }
  .brand__name {
    font-family: "Michroma", sans-serif;
    font-size: 26px;
    line-height: 1.4;
    letter-spacing: 1px;
    color: var(--orange);
    text-transform: uppercase;
    max-width: 420px;
  }
  .contact {
    position: absolute;
    right: 60px;
    bottom: 60px;
    display: flex;
    align-items: flex-end;
    gap: 20px;
  }
  .contact__person { text-align: right; line-height: 1.05; }
  .contact__name { color: var(--orange); font-size: 27px; font-weight: 500; text-transform: uppercase; }
  .contact__role { font-size: 27px; }
  .contact__divider { width: 1px; height: 66px; background: var(--steel); }
  .contact__details { font-size: 24px; line-height: 1.1; }

  .back__brand {
    position: absolute;
    left: 80px;
    right: 80px;
    top: 140px;
    display: flex;
    justify-content: center;
    align-items: center;
    gap: 16px;
  }
  .back__brand .brand__mark { width: 34px; height: 34px; }
  .back__brand .brand__name {
    font-size: 20px;
    white-space: nowrap;
    max-width: none;
  }
  .tagline {
    position: absolute;
    left: 80px;
    right: 80px;
    top: 235px;
    text-align: center;
    font-family: "Michroma", sans-serif;
    font-size: 15px;
    letter-spacing: 2px;
    text-transform: uppercase;
  }
</style>
</head>
<body>
  <section class="card card--front">
    <div class="brand">
      <span class="brand__mark"></span>
      <span class="brand__name">Kestrel Mark Construction</span>
    </div>
    <div class="contact">
      <div class="contact__person">
        <div class="contact__name">Owen Hartley</div>
        <div class="contact__role">President</div>
      </div>
      <div class="contact__divider"></div>
      <div class="contact__details">
        <div>owen@kestrelmark.example</div>
        <div>www.kestrelmark.example</div>
      </div>
    </div>
  </section>

  <section class="card card--back">
    <div class="back__brand">
      <span class="brand__mark"></span>
      <span class="brand__name">Kestrel Mark Construction</span>
    </div>
    <p class="tagline">Commercial Painting and Roofing</p>
  </section>
</body>
</html>
```